Coding for web page

need to have functions you designed coded as discussed, you have files.
Need client contact details box to enable me to receive client details to suggest events
Need quidlane/ payment page linked to ' book now' buttons
Need to be able to update upcoming events and re-write text as needed.

Industry/Entity Type

Events

```html
<!DOCTYPE html>
<html lang="en">
<head>
<meta charset="utf-8">
<title>Velvet Table Socials</title>
<link href="https://fonts.googleapis.com/css2?family=Open+Sans:wght@300;400;600&display=swap" rel="stylesheet">
<style>
:root{
  --ink:#0e0e0e;
  --gold:#c9a552;
  --gold-light:#e6cf8c;
  --gold-dark:#9c7a33;
  --grey-bg:#e4e4e4;
  --text:#555;
  --orange:#c9791e;
  --line:#d6d6d6;
  --white:#fff;
}
*{margin:0;padding:0;box-sizing:border-box}
html,body{width:820px;height:1200px;overflow:hidden}
body{font-family:"Open Sans",Arial,sans-serif;color:var(--text);position:relative;background:var(--grey-bg)}
.site-header{position:absolute;left:0;top:0;width:820px;height:95px;background:linear-gradient(#1a1a1a,#050505)}
.brand-plate{position:absolute;left:322px;top:0;width:175px;height:108px;background:#0a0a0a;border-radius:0 0 14px 14px;text-align:center;padding-top:30px;z-index:3}
.brand-mark{display:inline-block;width:12px;height:12px;border-radius:50%;background:var(--gold);margin-bottom:4px}
.brand-name{font-size:15px;font-weight:600;color:var(--gold);letter-spacing:1px;line-height:18px}
.brand-tag{font-size:9px;color:var(--gold-light);margin-top:2px}
.brand-phones{font-size:8px;color:#ddd;margin-top:6px;letter-spacing:.5px}
.header-contact{position:absolute;left:543px;top:32px;font-size:9px;color:var(--gold)}
.header-contact div{display:flex;align-items:center;gap:8px;height:17px}
.hero{position:absolute;left:0;top:95px;width:820px;height:325px;background:linear-gradient(100deg,#2b2520 0%,#4a3a30 35%,#6b4a3a 55%,#3a2a22 80%,#5a3a2e 100%)}
.hero-copy{position:absolute;left:107px;top:118px;color:var(--white)}
.hero-copy .line1{font-size:19px;font-weight:300}
.hero-copy .line2{font-size:28px;font-weight:300;line-height:34px}
.hero-copy b{font-weight:400}
.hero-cta{position:absolute;left:107px;top:190px;width:208px;height:34px;border:2px solid rgba(255,255,255,.75);border-radius:5px;background:rgba(0,0,0,.35);color:var(--white);font-size:15px;line-height:30px;text-align:center}
.intro{position:absolute;left:0;top:420px;width:820px;height:245px;background:linear-gradient(#ebebeb,#dedede)}
.intro h2{position:absolute;left:107px;top:36px;font-size:18px;font-weight:300;color:var(--gold-dark)}
.intro p{position:absolute;left:107px;top:76px;width:350px;font-size:10.3px;line-height:18.6px;text-align:justify}
.photo-circle{position:absolute;border-radius:50%;border:3px solid var(--white)}
.events-band{position:absolute;left:0;top:665px;width:820px;height:490px;background:linear-gradient(90deg,#3a2212,#6b4424 30%,#8a5a30 50%,#5a3a20 75%,#2a1a10)}
.ribbon{position:absolute;left:287px;top:643px;width:230px;height:38px;z-index:2}
.ribbon-label{position:absolute;left:327px;top:643px;width:150px;height:32px;line-height:32px;text-align:center;font-size:12px;color:#6b4c17;z-index:3}
.events-table{position:absolute;left:107px;top:715px;width:368px;height:410px;background:var(--white);border:1px solid #ccc}
.table-head{height:33px;background:#f2f2f2;border-bottom:1px solid var(--line);font-size:8.5px;color:var(--orange);position:relative}
.table-head span,.event-row span{position:absolute}
.event-row{height:63px;border-bottom:1px solid var(--line);position:relative;font-size:7.5px;line-height:12px}
.event-row:last-child{border-bottom:0}
.thumb{position:absolute;left:6px;top:12px;width:37px;height:37px;background:linear-gradient(135deg,#8a6a50,#d8c8b0);border-radius:2px}
.event-title{color:#333;font-size:8px}
.status{color:var(--orange)}
.book-btn{position:absolute;left:320px;top:31px;width:39px;height:12px;background:linear-gradient(#efd99a,#c9a552);border:1px solid var(--gold-dark);border-radius:2px;font-size:6.5px;line-height:10px;text-align:center;color:#5a4010}
.finder{position:absolute;left:511px;top:715px;width:201px;height:410px;background:var(--white);border:1px solid #ccc}
.finder-head{height:30px;background:#f2f2f2;border-bottom:1px solid var(--line);font-size:9.5px;color:#333;padding:9px 0 0 9px}
.finder-intro{font-size:7.5px;line-height:12px;padding:8px 9px;border-bottom:1px dotted #bbb;height:43px}
.field{position:absolute;left:0;width:201px;height:18px;font-size:8px}
.field label{position:absolute;right:116px;top:3px;white-space:nowrap}
.input{position:absolute;top:0;height:17px;border:1px solid #ccc;background:#f7f7f7;font-size:7px;color:#666;padding:3px 4px}
.select::after{content:"";position:absolute;right:4px;top:7px;border:3px solid transparent;border-top-color:#888}
.suggest-btn{position:absolute;left:9px;top:369px;width:184px;height:27px;background:linear-gradient(#f0dc9e,#c9a552);border:1px solid var(--gold-dark);border-radius:4px;font-size:11px;line-height:25px;text-align:center;color:#6b4c17}
.site-footer{position:absolute;left:0;top:1155px;width:820px;height:45px;background:#e2e2e2;font-size:7px;color:#777}
.site-footer .left{position:absolute;left:107px;top:16px}
.site-footer .right{position:absolute;left:447px;top:16px}
</style>
</head>
<body>
<header class="site-header">
  <div class="brand-plate">
    <div class="brand-mark"></div>
    <div class="brand-name">VELVET TABLE</div>
    <div class="brand-tag">Real people · Real opportunities</div>
    <div class="brand-phones">B:0871004415 M:0491226037</div>
  </div>
  <div class="header-contact">
    <div><svg width="10" height="10" viewBox="0 0 10 10"><circle cx="5" cy="5" r="5" fill="#c9a552"/><path d="M3 2.5l1 1-0.6 0.8c.4.8 1 1.4 1.8 1.8l.8-.6 1 1-.8.9C4.5 7.3 2.7 5.5 2.3 3.3z" fill="#111"/></svg>08 7100 4415 - 0491226037</div>
    <div><svg width="10" height="10" viewBox="0 0 10 10"><circle cx="5" cy="5" r="5" fill="#c9a552"/><rect x="2.5" y="3.2" width="5" height="3.6" fill="#111"/><path d="M2.5 3.2l2.5 2 2.5-2" stroke="#c9a552" stroke-width=".6" fill="none"/></svg>hello@velvettablesocials.example</div>
  </div>
</header>

<section class="hero" role="img" aria-label="Photo of a smartly dressed couple smiling over a menu at a candlelit restaurant table">
  <div class="hero-copy">
    <div class="line1">Have fun while <b>dating</b></div>
    <div class="line2">with a touch of <b>class</b></div>
  </div>
  <div class="hero-cta">Check out upcoming events</div>
</section>

<section class="intro">
  <h2>Your soul mate could be at the next table</h2>
  <p>Velvet Table Socials is an elegant and sophisticated speed dating organisation. New to Adelaide, we aim to provide a service where you feel pampered and have fun while ‘dating’ with a touch of class! With extensive dating industry experience in Adelaide and North America, founder Miriam Lowell, has a passion for introducing singles. So, let’s get out there and date with speed! Your soul mate could be at the next table!</p>
  <div class="photo-circle" role="img" aria-label="Photo of a couple toasting at dinner" style="left:505px;top:33px;width:112px;height:112px;background:radial-gradient(#b88a6a,#4a3024)"></div>
  <div class="photo-circle" role="img" aria-label="Photo of a couple embracing outdoors" style="left:600px;top:75px;width:110px;height:110px;background:radial-gradient(#c8c0b8,#3a3a48)"></div>
  <div class="photo-circle" role="img" aria-label="Photo of a candlelit dinner table" style="left:538px;top:120px;width:80px;height:80px;background:radial-gradient(#e0b070,#5a3010)"></div>
</section>

<section class="events-band" role="img" aria-label="Photo of a warmly lit restaurant dining room"></section>

<svg class="ribbon" viewBox="0 0 230 38">
  <polygon points="0,8 42,8 42,36 0,36 14,22" fill="#b8933f"/>
  <polygon points="230,8 188,8 188,36 230,36 216,22" fill="#b8933f"/>
  <rect x="40" y="0" width="150" height="32" fill="#e3c97f"/>
</svg>
<div class="ribbon-label">UPCOMING EVENTS</div>

<div class="events-table">
  <div class="table-head">
    <span style="left:7px;top:12px">Event type &amp; city</span>
    <span style="left:153px;top:12px">Date &amp; Time</span>
    <span style="left:213px;top:12px">Age</span>
    <span style="left:260px;top:12px">Status</span>
    <span style="left:320px;top:12px">Price</span>
  </div>
  <div class="event-row"><div class="thumb" role="img" aria-label="Venue photo"></div><span style="left:51px;top:10px"><span class="event-title" style="position:static">Speed dating with style</span><br>Linden Restaurant<br>Adelaide</span><span style="left:153px;top:10px">04.26.2014<br>7.00pm</span><span style="left:213px;top:10px">M : 40-50<br>F : 35-42</span><span class="status" style="left:260px;top:10px">2 spaces left</span><span style="left:320px;top:10px">$ 95.20</span><div class="book-btn">Book now</div></div>
  <div class="event-row"><div class="thumb" role="img" aria-label="Venue photo"></div><span style="left:51px;top:10px"><span class="event-title" style="position:static">Tall men speed dating</span><br>The Harbourline Hotel<br>Adelaide</span><span style="left:153px;top:10px">05.03.2014<br>10.00pm</span><span style="left:213px;top:10px">M : 30-40<br>F : 25-35</span><span class="status" style="left:260px;top:10px">1 spaces left</span><span style="left:320px;top:10px">$ 87.15</span><div class="book-btn">Book now</div></div>
  <div class="event-row"><div class="thumb" role="img" aria-label="Venue photo"></div><span style="left:51px;top:10px"><span class="event-title" style="position:static">Single’s party</span><br>Bar 212, West<br>Adelaide</span><span style="left:153px;top:10px">04.26.2014<br>7.00pm</span><span style="left:213px;top:10px">M : 40-50<br>F : 35-42</span><span class="status" style="left:260px;top:10px">2 spaces left</span><span style="left:320px;top:10px">$ 95.20</span><div class="book-btn">Book now</div></div>
  <div class="event-row"><div class="thumb" role="img" aria-label="Venue photo"></div><span style="left:51px;top:10px"><span class="event-title" style="position:static">Speed dating with style</span><br>Linden Restaurant<br>Adelaide</span><span style="left:153px;top:10px">04.26.2014<br>7.00pm</span><span style="left:213px;top:10px">M : 40-50<br>F : 35-42</span><span class="status" style="left:260px;top:10px">2 spaces left</span><span style="left:320px;top:10px">$ 95.20</span><div class="book-btn">Book now</div></div>
  <div class="event-row"><div class="thumb" role="img" aria-label="Venue photo"></div><span style="left:51px;top:10px"><span class="event-title" style="position:static">Speed dating with style</span><br>Linden Restaurant<br>Adelaide</span><span style="left:153px;top:10px">04.26.2014<br>7.00pm</span><span style="left:213px;top:10px">M : 40-50<br>F : 35-42</span><span class="status" style="left:260px;top:10px">2 spaces left</span><span style="left:320px;top:10px">$ 95.20</span><div class="book-btn">Book now</div></div>
  <div class="event-row"><div class="thumb" role="img" aria-label="Venue photo"></div><span style="left:51px;top:10px"><span class="event-title" style="position:static">Speed dating with style</span><br>Linden Restaurant<br>Adelaide</span><span style="left:153px;top:10px">04.26.2014<br>7.00pm</span><span style="left:213px;top:10px">M : 40-50<br>F : 35-42</span><span class="status" style="left:260px;top:10px">2 spaces left</span><span style="left:320px;top:10px">$ 95.20</span><div class="book-btn">Book now</div></div>
</div>

<div class="finder">
  <div class="finder-head">Let us find you the perfect event</div>
  <div class="finder-intro">Tell us a bit about yourself to see speed dating &amp; singles events that suit you. It’s free !</div>
  <div class="field" style="top:81px"><label>My name is :</label><div class="input" style="left:90px;width:103px"></div></div>
  <div class="field" style="top:105px"><label>I was born on :</label><div class="input select" style="left:90px;width:29px">MM</div><div class="input select" style="left:122px;width:29px">DD</div><div class="input select" style="left:154px;width:39px">YY</div></div>
  <div class="field" style="top:130px"><label>I live in :</label><div class="input select" style="left:90px;width:103px">Please select one</div></div>
  <div class="field" style="top:154px"><label>I am :</label><div class="input select" style="left:90px;width:103px">Please select one</div></div>
  <div class="field" style="top:178px"><label>Aged between :</label><div class="input select" style="left:90px;width:41px">Select</div><span style="position:absolute;left:136px;top:3px">and</span><div class="input select" style="left:152px;width:41px">Select</div></div>
  <div class="field" style="top:203px"><label>My education level :</label><div class="input select" style="left:90px;width:103px">Please select one</div></div>
  <div class="field" style="top:227px"><label>I am a :</label><div class="input select" style="left:90px;width:103px">Please select one</div></div>
  <div class="field" style="top:252px"><label>My height is :</label><div class="input select" style="left:90px;width:103px">Please select one</div></div>
  <div class="field" style="top:277px"><label>Mobile phone :</label><div class="input" style="left:90px;width:103px"></div></div>
  <div class="field" style="top:301px"><label>Email :</label><div class="input" style="left:90px;width:103px"></div></div>
  <div class="field" style="top:326px"><label>Password :</label><div class="input" style="left:90px;width:103px"></div></div>
  <div class="suggest-btn">SUGGEST ME AN EVENT</div>
</div>

<footer class="site-footer">
  <span class="left">© 2014 Velvet Table Socials | All rights reserved</span>
  <span class="right">Phone : 08 7100 4415 - 0491226037 &nbsp;&nbsp; Email : hello@velvettablesocials.example</span>
</footer>
</body>
</html>
```